Business Card Design

Please copy the format of the attached card.

FRONT:
White text small blue horses head logo where "mirun" in in example

BACK:
Blue background w/ white horses head

Industry/Entity Type

Business

Contact Information for Business Card

Calvin Ostrow
Chief Executive Officer
Halvern Lodges & Resorts
412 Lindmoor Street | Alderport, Westmara 90417
Tel: +1.555.482.1937
email: calvin@halvernlodges.example

```html
<!DOCTYPE html>
<html lang="en">
<head>
<meta charset="utf-8">
<title>Halvern Lodges &amp; Resorts – Business Card</title>
<link rel="stylesheet" href="https://fonts.googleapis.com/css2?family=Source+Sans+3:wght@400;600&display=swap">
<style>
  :root {
    --brand-blue: #13508a;
    --ink: #1c2733;
    --paper: #ffffff;
    --backdrop: #9a9a9a;
    --card-w: 700px;
    --card-h: 400px;
  }
  * { box-sizing: border-box; margin: 0; padding: 0; }
  html, body {
    width: 1200px;
    height: 900px;
    overflow: hidden;
    background: var(--backdrop);
    font-family: "Source Sans 3", "Myriad Pro", Arial, sans-serif;
  }
  .sheet {
    width: 1200px;
    height: 900px;
    display: flex;
    flex-direction: column;
    align-items: center;
    justify-content: center;
    gap: 40px;
  }
  .card {
    width: var(--card-w);
    height: var(--card-h);
    position: relative;
  }
  .card--front {
    background: var(--paper);
    color: var(--ink);
    padding: 40px 44px;
  }
  .contact,
  .identity {
    font-size: 24px;
    line-height: 1.15;
  }
  .identity {
    margin-top: 22px;
  }
  .identity__name {
    color: var(--brand-blue);
    font-weight: 600;
  }
  .brand-mark {
    display: flex;
    align-items: center;
    gap: 10px;
    font-weight: 600;
  }
  .card--front .brand-mark {
    position: absolute;
    right: 44px;
    bottom: 70px;
    color: var(--brand-blue);
    font-size: 30px;
  }
  .brand-mark__dot {
    width: 16px;
    height: 16px;
    border-radius: 50%;
    background: currentColor;
  }
  .card--back {
    background: var(--brand-blue);
    color: var(--paper);
    display: flex;
    align-items: center;
    justify-content: center;
  }
  .card--back .brand-mark {
    font-size: 64px;
    gap: 18px;
  }
  .card--back .brand-mark__dot {
    width: 30px;
    height: 30px;
  }
</style>
</head>
<body>
<main class="sheet">
  <section class="card card--front" aria-label="Card front">
    <div class="contact">
      <p>412 Lindmoor Street | Alderport, Westmara 90417</p>
      <p>Tel: +1.555.482.1937</p>
      <p>email: calvin@halvernlodges.example</p>
    </div>
    <div class="identity">
      <p class="identity__name">Calvin Ostrow</p>
      <p>Chief Executive Officer</p>
      <p>Halvern Lodges &amp; Resorts</p>
    </div>
    <div class="brand-mark">
      <span class="brand-mark__dot"></span>
      <span>Halvern</span>
    </div>
  </section>
  <section class="card card--back" aria-label="Card back">
    <div class="brand-mark">
      <span class="brand-mark__dot"></span>
      <span>Halvern</span>
    </div>
  </section>
</main>
</body>
</html>
```